New Podcast focussing on non-mainstream interventions for guidance needs podcast art

I need an exquisite piece of podcast art work for the launch of my new podcast 'Beyond the Still'. This podcast explores unorthodox, esoteric and unconventional methods to find peace, clarity and direction in life. Topics include family Constellations Systems, Psychedelics, Equine Therapy and Floatation to name a few. A teaser has been posted on Talvora with a strong response. The audience is primarily midlifers or those in a career/personal crisis of direction. It's meant to comfort, inform and empower and offer other ways rather than mainstream to work out what to do with your life. The file shared with you shows the pic used on Talvora as it's illustrating the idea of illumination. You can use it or not, and whilst I am ex-Military, I don't want the cover to convey an overly military influence. I'd like 'Beyond the Still' to feature on the art work and my name, Mirela Dunford. I'd like inspiration, creativity, and the idea of hope conveyed as well as clarity and courage. Whilst the podcast is about finding your direction please do no use compass images or cross road images as that is too obvious.
Hope that all helps. Looking forward to your ideas.

```html
<!DOCTYPE html>
<html lang="en">
<head>
<meta charset="utf-8">
<title>Beyond the Still — Mirela Dunford</title>
<link rel="stylesheet" href="https://fonts.googleapis.com/css2?family=Montserrat:wght@600&display=swap">
<style>
  :root {
    --bg: #000000;
    --text: #ffffff;
    --swirl-core: #2a1018;
    --swirl-ring: #5a2a36;
    --swirl-glow: #6a3a30;
    --swirl-edge: rgba(0, 0, 0, 0);
    --bloom-centre: #c9866a;
    --bloom-heart-edge: #8a3a4a;
    --bloom-inner: #d27ab8;
    --bloom-copper: #d9977a;
    --bloom-mid: #a02a78;
    --bloom-deep: #6a1048;
    --bloom-outer: #b04a98;
    --bloom-rim: #c0187a;
  }
  html, body {
    margin: 0;
    padding: 0;
    background: var(--bg);
    overflow: hidden;
  }
  .cover {
    position: relative;
    width: 1200px;
    height: 1200px;
    background: var(--bg);
    overflow: hidden;
    font-family: "Montserrat", sans-serif;
  }
  .corner-swirls,
  .central-bloom {
    position: absolute;
    left: 0;
    top: 0;
    width: 1200px;
    height: 1200px;
  }
  .cover-text {
    position: absolute;
    left: 0;
    width: 1200px;
    margin: 0;
    text-align: center;
    color: var(--text);
    font-weight: 600;
    line-height: 1;
    letter-spacing: 0;
    white-space: nowrap;
  }
  .host-name { top: 58px; font-size: 86px; }
  .show-title { top: 1028px; font-size: 100px; }
</style>
</head>
<body>
  <main class="cover">
    <svg class="corner-swirls" viewBox="0 0 1200 1200" role="img" aria-label="Four dark plum and bronze spiral ornaments, one in each corner">
      <defs>
        <radialGradient id="swirl-fill">
          <stop offset="0" stop-color="var(--swirl-core)"/>
          <stop offset="0.3" stop-color="var(--swirl-ring)" stop-opacity="0.8"/>
          <stop offset="0.45" stop-color="var(--swirl-core)" stop-opacity="0.7"/>
          <stop offset="0.7" stop-color="var(--swirl-glow)" stop-opacity="0.7"/>
          <stop offset="0.88" stop-color="var(--swirl-ring)" stop-opacity="0.4"/>
          <stop offset="1" stop-color="var(--swirl-edge)"/>
        </radialGradient>
      </defs>
      <circle cx="175" cy="190" r="215" fill="url(#swirl-fill)"/>
      <circle cx="1025" cy="190" r="215" fill="url(#swirl-fill)"/>
      <circle cx="165" cy="1040" r="215" fill="url(#swirl-fill)"/>
      <circle cx="1030" cy="1040" r="215" fill="url(#swirl-fill)"/>
    </svg>

    <svg class="central-bloom" viewBox="0 0 1200 1200" role="img" aria-label="Layered magenta mandala flower with a ribbed copper heart at its centre">
      <defs>
        <radialGradient id="bloom-fill">
          <stop offset="0" stop-color="var(--bloom-centre)"/>
          <stop offset="0.16" stop-color="var(--bloom-heart-edge)"/>
          <stop offset="0.24" stop-color="var(--bloom-inner)"/>
          <stop offset="0.36" stop-color="var(--bloom-copper)"/>
          <stop offset="0.46" stop-color="var(--bloom-mid)"/>
          <stop offset="0.7" stop-color="var(--bloom-deep)"/>
          <stop offset="0.88" stop-color="var(--bloom-outer)"/>
          <stop offset="1" stop-color="var(--bloom-deep)"/>
        </radialGradient>
      </defs>
      <circle cx="600" cy="600" r="438" fill="url(#bloom-fill)" stroke="var(--bloom-rim)" stroke-width="2"/>
    </svg>

    <h2 class="cover-text host-name">Mirela Dunford</h2>
    <h1 class="cover-text show-title">Beyond the Still</h1>
  </main>
</body>
</html>
```